IT’S NOT A CLEANING, IT’S YOUR LIFE! TOP TEN REASONS WHY THIS IS NOT JUST A “CLEANING”

We made a list for our patients to let them know why our hygiene appointments are different than other cleanings. Since this is a lot of information, we would like it easily readable within 4-5 feet but we do not want the post to be HUGE. Please see below:

IT’S NOT A CLEANING, IT’S YOUR LIFE!
TOP TEN REASONS WHY THIS IS NOT JUST A “CLEANING”

10. We make you look better. Healthy teeth and gums are more attractive. Recent studies
show that the smile is the first thing people notice and that people with better looking teeth
are more confident and successful.

9. We can relieve your headaches. During your hygiene visit we evaluate for serious bite
issues, many of which lead to muscle soreness, headaches, and migraines.

8. We check for oral cancer. Oral cancer kills 1 person per hour 24 hours a day. The death rate for oral cancer is higher than cancers we routinely hear about such as cervical, thyroid and skin cancer.

7. We make you smell better. During your hygiene visit we eliminate many of the germs that live under your gum tissue and cause bad breath.

6. We save you money. By utilizing the latest dental technology (digital x-rays, mouth
cameras, and magnification glasses) we can help with early detection of tooth and gum
problems and save you the cost of gum surgery, root canals, and implants.

5. We clean in places you cannot. We clean under the gum line and between teeth where
most of the germs hide and cause dental disease. 40% of the bacteria in your mouth lives in
between your teeth.

4. We prevent pain. We identify tooth decay that can lead to nerve involvement and pain,
root canal, and tooth loss.

3. We save your teeth. Most tooth loss is from periodontal/gum disease. At each visit we
evaluate the health of your gums and bone with our periodontal screening. Periodontal
disease, like high blood pressure, is symptomless until it is in advanced stages.

2. We protect your loved ones. Studies have proven that the bacteria that cause dental
disease can be transmitted from person to person. Think about that the next time you kiss
someone!

1. We prolong life. Researchers have linked the inflammation and infection found in the
mouth to heart attacks, strokes, and Alzheimer’s. By reducing infection in your mouth we can
greatly improve your overall health!

```html
<!DOCTYPE html>
<html lang="en">
<head>
<meta charset="utf-8">
<title>It's Not a Cleaning, It's Your Life!</title>
<link href="https://fonts.googleapis.com/css2?family=Titillium+Web:wght@700&family=Open+Sans:wght@400;700&display=swap" rel="stylesheet">
<style>
  :root {
    --white: #ffffff;
    --ink: #2f2f2f;
    --number: #7a7a7a;
    --photo-dark: #6f7174;
    --photo-mid: #9a9c9f;
    --photo-light: #b9bbbd;
    --band-dark: #6b6b6b;
    --band-light: #ececec;
  }
  * { margin: 0; padding: 0; box-sizing: border-box; }
  html, body { width: 951px; height: 1200px; overflow: hidden; background: var(--white); }
  .poster { position: relative; width: 951px; height: 1200px; background: var(--white); font-family: "Open Sans", Arial, sans-serif; }

  .hero {
    position: absolute; left: 0; top: 0; width: 951px; height: 437px;
    background: radial-gradient(ellipse at 50% 40%, var(--photo-light) 0%, var(--photo-mid) 45%, var(--photo-dark) 100%);
  }
  .headline {
    position: absolute; left: 58px; top: 100px;
    display: flex; align-items: flex-end;
    font-family: "Titillium Web", Arial, sans-serif; font-weight: 700; color: var(--white);
  }
  .headline-big { font-size: 54px; line-height: 46px; letter-spacing: 0.5px; }
  .headline-small { font-size: 19.5px; line-height: 20px; margin-left: 5px; margin-bottom: 2px; }

  .banner {
    position: absolute; left: 179px; top: 470px; width: 772px; height: 76px;
    background: linear-gradient(90deg, var(--band-dark) 0%, #9a9a9a 45%, var(--band-light) 100%);
    padding: 15px 0 0 19px;
    color: var(--white); font-size: 18px; line-height: 23px;
  }
  .banner strong { font-weight: 700; }

  .reason { position: absolute; }
  .reason-number {
    position: absolute; left: 0; top: -4px;
    font-family: "Open Sans", Arial, sans-serif; font-weight: 700; font-size: 24px; color: var(--number);
  }
  .reason-text {
    position: absolute; left: 49px; top: 0;
    font-size: 12.4px; line-height: 15.6px; color: var(--ink);
  }
  .col-left { left: 130px; }
  .col-left .reason-text { width: 250px; }
  .col-right { left: 488px; }
  .col-right .reason-text { width: 266px; }
</style>
</head>
<body>
<main class="poster">
  <section class="hero" role="img" aria-label="Photo of a woman in a white blouse holding a printed picture of a wide smile in front of her face, against a grey wall"></section>
  <h1 class="headline">
    <span class="headline-big">IT’S</span>
    <span class="headline-small">NOT A CLEANING,<br>YOUR LIFE!</span>
  </h1>

  <h2 class="banner">TOP TEN REASONS WHY<br>THIS IS NOT JUST A “<strong>CLEANING</strong>”</h2>

  <div class="reason col-left" style="top:591px">
    <span class="reason-number">10</span>
    <p class="reason-text">We make you look better. Healthy teeth and gums are more attractive. Recent studies show that the smile is the first thing people notice and that people with better looking teeth are more confident and successful</p>
  </div>
  <div class="reason col-right" style="top:591px">
    <span class="reason-number">09</span>
    <p class="reason-text">We can relieve your headaches. During your hygiene visit we evaluate for serious bite issues, many of which lead to muscle soreness, headaches, and migraines</p>
  </div>

  <div class="reason col-left" style="top:707px">
    <span class="reason-number">08</span>
    <p class="reason-text">We check for oral cancer. Oral cancer kills 1 person per hour 24 hours a day. The death rate for oral cancer is higher than cancers we routinely hear about such as cervical, thyroid and skin cancer</p>
  </div>
  <div class="reason col-right" style="top:707px">
    <span class="reason-number">07</span>
    <p class="reason-text">We make you smell better. During your hygiene visit we eliminate many of the germs that live under your gum tissue and cause bad breath.</p>
  </div>

  <div class="reason col-left" style="top:823px">
    <span class="reason-number">06</span>
    <p class="reason-text">We save you money. By utilizing the latest dental technology (digital x-rays, mouth cameras, and magnification glasses) we can help with early detection of tooth and gum problems and save you the cost of gum surgery, root canals, and implants</p>
  </div>
  <div class="reason col-right" style="top:823px">
    <span class="reason-number">05</span>
    <p class="reason-text">We clean in places you cannot. We clean under the gum line and between teeth where most of the germs hide and cause dental disease. 40% of the bacteria in your mouth lives in between your teeth.</p>
  </div>

  <div class="reason col-left" style="top:951px">
    <span class="reason-number">04</span>
    <p class="reason-text">We prevent pain. We identify tooth decay that can lead to nerve involvement and pain, root canal, and tooth loss.</p>
  </div>
  <div class="reason col-right" style="top:951px">
    <span class="reason-number">03</span>
    <p class="reason-text">We save your teeth. Most tooth loss is from periodontal/gum disease. At each visit we evaluate the health of your gums and bone with our periodontal screening. Periodontal disease, like high blood pressure, is symptomless until it is in advanced stages.</p>
  </div>

  <div class="reason col-left" style="top:1075px">
    <span class="reason-number">02</span>
    <p class="reason-text">We protect your loved ones. Studies have proven that the bacteria that cause dental disease can be transmitted from person to person. Think about that the next time you kiss someone!</p>
  </div>
  <div class="reason col-right" style="top:1075px">
    <span class="reason-number">01</span>
    <p class="reason-text">We prolong life. Researchers have linked the inflammation and infection found in the mouth to heart attacks, strokes, and Alzheimer’s. By reducing infection in your mouth we can greatly improve your overall health!</p>
  </div>
</main>
</body>
</html>
```